Infill Flyer

We would like a flyer designed.

8.5 inches x 11 inches

Clean, fresh, professional, scientific look

I realize that a few of my photos are not high resolution, but I will be using this for electronic transmission for now. Thanks!

Industry/Entity Type

Electronic

Font styles to use
Sans Serif

```html
<!DOCTYPE html>
<html lang="en">
<head>
<meta charset="utf-8">
<title>FieldGrass – Infill Flyer</title>
<link href="https://fonts.googleapis.com/css2?family=Arimo:wght@400;700&family=Open+Sans:wght@400&family=Lato:wght@400;700&display=swap" rel="stylesheet">
<style>
  :root {
    --green: #6ab344;
    --green-dark: #4e9a2e;
    --turf-light: #8fd24f;
    --turf-mid: #4f9a2c;
    --wall: #1f4a2e;
    --rubber: #1c1c1c;
    --grey-head: #6d6d6d;
    --ink: #1a1a1a;
    --white: #ffffff;
  }
  * { margin: 0; padding: 0; box-sizing: border-box; }
  html, body { width: 900px; height: 1200px; overflow: hidden; background: var(--white); }
  .flyer { position: relative; width: 900px; height: 1200px; overflow: hidden; background: var(--white); }

  .hero { position: absolute; left: 0; top: 0; width: 900px; height: 600px; }

  .brand {
    position: absolute; left: 42px; top: 52px;
    display: flex; align-items: center; gap: 12px;
    font-family: "Arimo", sans-serif; font-weight: 700; font-size: 52px;
    color: var(--green); letter-spacing: -1px;
  }
  .brand-mark { width: 26px; height: 26px; background: var(--green); }

  .rubber-photo {
    position: absolute; left: 538px; top: 325px; width: 252px; height: 252px;
    border-radius: 50%; border: 5px solid var(--green);
    background: radial-gradient(circle at 50% 45%, #3a3a3a 0%, var(--rubber) 60%, #2b2b2b 70%, #f4f4f4 71%);
  }

  .intro-title {
    position: absolute; left: 42px; top: 582px; width: 422px; height: 94px;
    background: var(--green); color: var(--white);
    font-family: "Arimo", sans-serif; font-weight: 700;
    padding: 12px 14px 0 18px; line-height: 1.25;
  }
  .intro-title .line1 { font-size: 22px; display: block; }
  .intro-title .line2 { font-size: 27px; display: block; }

  .intro-text {
    position: absolute; left: 42px; top: 694px; width: 422px;
    font-family: "Open Sans", sans-serif; font-size: 19.5px; line-height: 1.37;
    color: var(--ink); text-align: justify;
  }

  .controversy-title {
    position: absolute; left: 502px; top: 605px; width: 380px;
    font-family: "Arimo", sans-serif; font-weight: 700; font-size: 23px; line-height: 1.38;
    color: var(--grey-head);
  }
  .controversy-text {
    position: absolute; left: 505px; top: 690px; width: 362px;
    font-family: "Arimo", sans-serif; font-size: 15.6px; line-height: 1.3;
    color: var(--ink); text-align: justify;
  }

  .options-band { position: absolute; left: 0; top: 925px; width: 900px; height: 275px; }

  .infill-photo {
    position: absolute; left: 64px; top: 963px; width: 206px; height: 206px;
    border-radius: 50%; border: 5px solid var(--white);
    background: radial-gradient(circle at 50% 50%, #2f5a2f 0%, #1e3a22 65%, #e9e9e9 66%);
  }

  .options-title {
    position: absolute; left: 318px; top: 1000px;
    font-family: "Arimo", sans-serif; font-weight: 700; font-size: 23px;
    color: var(--white);
  }
  .options-text {
    position: absolute; left: 320px; top: 1042px; width: 548px;
    font-family: "Lato", sans-serif; font-size: 18.6px; line-height: 1.33;
    color: var(--white);
  }
</style>
</head>
<body>
<div class="flyer">

  <svg class="hero" viewBox="0 0 900 600" role="img" aria-label="Photo of an indoor training hall with striped green artificial turf and dark green curtains">
    <defs>
      <linearGradient id="hallGradient" x1="0" y1="0" x2="0" y2="1">
        <stop offset="0" stop-color="#2c5a3a"/>
        <stop offset="0.5" stop-color="var(--wall)"/>
        <stop offset="0.62" stop-color="#5fae36"/>
        <stop offset="1" stop-color="var(--turf-light)"/>
      </linearGradient>
    </defs>
    <path d="M0 140 C 220 150, 420 60, 620 40 C 760 28, 850 20, 900 20 L900 520 C 760 540, 640 600, 500 585 C 330 570, 180 560, 0 540 Z" fill="url(#hallGradient)"/>
    <g fill="none" stroke="var(--white)" stroke-width="2">
      <path d="M0 136 C 220 146, 420 56, 620 36 C 760 24, 850 16, 900 16"/>
      <path d="M0 128 C 220 138, 420 48, 620 28 C 760 16, 850 8, 900 8"/>
      <path d="M0 120 C 220 130, 420 40, 620 20 C 760 8, 850 0, 900 0"/>
    </g>
    <path d="M0 540 C 180 560, 330 570, 500 585 C 640 600, 760 540, 900 520 L900 600 L0 600 Z" fill="var(--white)"/>
  </svg>

  <div class="brand"><span class="brand-mark"></span>FieldGrass</div>

  <div class="rubber-photo" role="img" aria-label="Close-up photo of a pile of black crumb rubber granules"></div>

  <h2 class="intro-title"><span class="line1">The Scoop on Crumb Rubber</span><span class="line2">and Other Infill Options</span></h2>
  <p class="intro-text">There are lots of infill options. The most commonly used infill used is crumb rubber from recycled tires. You might have heard some rumors floating around about crumb rubber, so we’re here to fill you in on what you need to know. So if you’re curious here’s the story.</p>

  <h2 class="controversy-title">What is the controversy and why are people concerned?</h2>
  <p class="controversy-text">Recently, a soccer coach in Washington State became understandably concerned when two of her goalkeepers were diagnosed with cancer. Through her network of contacts she conducted an informal poll and found more cases of cancer among soccerplayers – 38 in all, with a dozen in Washington. The coach wondered if the cancer was caused by crumb rubber in ynthetic turf. When Channel 9 News picked up the story, a lot of questions arose.</p>

  <svg class="options-band" viewBox="0 0 900 275" aria-hidden="true">
    <path d="M0 30 L60 22 L140 28 L220 18 L300 26 L360 14 L420 24 L470 10 L520 22 L600 16 L680 24 L740 12 L800 22 L860 16 L900 20 L900 275 L0 275 Z" fill="var(--green)"/>
  </svg>

  <div class="infill-photo" role="img" aria-label="Photo of a tray of dark green coated infill granules"></div>

  <h2 class="options-title">Are there other infill options?</h2>
  <p class="options-text">Yes. There are many other infill options. However, there are drawbacks to everything. And, frankly, nothing has been tested to the extent that crumb rubber has, especially for the price. As a point of comparison SBR sells for around $0.20 per pound.</p>

</div>
</body>
</html>
```